physio rehab flyer for Vela Motion please

Specification:
Flyer is to be trifold from letter size (8.5 x 11)
-----------------------This may help you:--------------------------
I would like the look of :
clean, minimalistic look with mainly blue and green
san serif font
professional
The colors I like are blue (not the blue in the logo enclosed, I want a change, but more like the blue on my website logo) and light green.
This is my website: www.velamotiongroup.ca just so you get an idea but it will be totally changed soon to a to be determined design.
I like the blue and green in file "sample 2" (enclosed)
I like the pictures in "sample 2" file enclosed
For inspiration, I like design of this brochure: http://www.qlx.ca/HarbourRestore/PatientsFamilies/Clinics_Tests/DAWL_Service/Documents/Brochure.pdf
Here's how I see the pages layout:
----[location: this should be the cover (outside, right panel of trifold)]-----
Vela Motion Logo
Integrated Injury Rehab
Evidence-based, one-on-one care to make your recovery fast and comfortable
www.velamotiongroup.ca
---------------[location: inside, left panel]----------------------------------------
Our team leaders
[portrait here]
Harriet Osei, MD, FRCPC, MSC, CIME
Physiatrist
Dr. Osei specializes in injury rehab and sports medicine. She is highly trained having received her MD and Residency in Physiatry from Wexmoor University. Her passion is to help injured people get back to their life.
[portrait here]
Dorothy Varga, PT
Physiotherapist
Dorothy has over 10 years of experience as a Physiotherapist (5 in Canada). She has advanced training in orthopedics and manual therapy. She loves and relates well with people from the youngest to the most senior.
--------------------[location: inside, middle panel]-------------------------------
Our services
We provide integrated assessment and care from interprofessional team of regulated healthcare professionals with proven experience in injury rehabilitation:
physiatrists
sport medicine physicians
physiotherapists
chiropractors
massage therapists
acupuncturists
psychologists
We provide custom medical bracing, orthotics, orthopedic shoes, assistive devices, and medical stockings, all in one place.
----------------------[location: inside, right panel]-----------------------------------
Only registered physiotherapists
We strongly believe in consistency with your treatment plan. This means that you spend your time here one-on-one with your physiotherapist, not any students or assistants. You get consistent high quality care from a professional.
One-on-one attention
We book maximum 3 people per hour to ensure everyone gets adequate one-on-one time with their physiotherapist. This compares favorably with other clinics, who may book upwards of 5-6 per hour. The atmosphere is professional -balanced with friendly, caring and relaxed. Our highly qualified staff operate this way to help make your recovery faster and more enjoyable.
------------------------[location: outside, left panel]---------------------------------
The right rehab for your clients
Timely access to comprehensive assessment and treatment
Proven track record in injury rehabilitation
Convenient one-stop service
Customized treatment plans
Integrated, co-ordinated care
Evidence-based care applying leading best practices
Access to specialty clinics: Physiatry and Chronic Pain
-------------------------[location: outside, middle panel]--------------------------
Please call us 416-738-4062
for more information on injury rehabilitation
Vela Motion Group
8120 Tolliver Rd., Unit 9
Scarborough, ON M4K 8B2
[Please include a line art map designed based on "map" file enclosed]
To make a referral for your clients, contact velamotiongroup@brisklane.ca or fax: 416-738-4059. Thank you.
www.velamotiongroup.ca
------------------------------------------------------------------------------------------------
Target Market(s)
family doctors, ER docs, lawyers, and general public age (20-50)
Industry/Entity Type
Health And Wellness
Requirements
Must have
- san serif font
- blue and green colors
- clean, sophisticated look
Nice to have
- consumer choice award badge either on front or back of trifold
Should not have
- see above

```html
<!DOCTYPE html>
<html lang="en">
<head>
<meta charset="utf-8">
<title>Vela Motion Group – Inside Spread</title>
<link rel="stylesheet" href="https://fonts.googleapis.com/css2?family=Open+Sans:wdth,wght@75..100,400..700&display=swap">
<style>
  :root {
    --blue: #5b8ac6;
    --blue-band: #6e9bd3;
    --grey-band: #a9abae;
    --text: #7a7c80;
    --list: #808285;
    --rule: #6b6b6b;
    --paper: #ffffff;
    --photo-light: #e9e9e9;
    --photo-dark: #3a3a3a;
    --badge: #dcdcdc;
  }
  * { box-sizing: border-box; margin: 0; padding: 0; }
  html, body { width: 1200px; height: 928px; overflow: hidden; background: var(--paper); }
  body { font-family: "Open Sans", Arial, sans-serif; color: var(--text); font-stretch: 90%; }
  .spread { position: relative; width: 1200px; height: 928px; background: var(--paper); }
  .fold { position: absolute; top: 0; width: 1px; height: 928px; background: var(--rule); }
  .fold--one { left: 399px; }
  .fold--two { left: 799px; }

  /* Left panel: team */
  .team-title { position: absolute; left: 83px; top: 58px; font-size: 27px; font-weight: 700; color: var(--blue); letter-spacing: -0.2px; font-stretch: 96%; }
  .name-band { position: absolute; left: 0; width: 400px; height: 84px; }
  .name-band--blue { top: 182px; background: var(--blue-band); }
  .name-band--grey { top: 528px; background: var(--grey-band); }
  .portrait { position: absolute; left: 35px; width: 123px; border-radius: 14px 14px 14px 40px; border: 3px solid #e6e8ec; }
  .portrait--doctor { top: 140px; height: 149px; background: linear-gradient(160deg, #b88a6a 0%, #d9d2cc 55%, #f2f2f2 100%); }
  .portrait--physio { top: 505px; height: 150px; background: linear-gradient(160deg, #9aa6b0 0%, #c79b8a 50%, #d7b3c0 100%); }
  .person-name { position: absolute; left: 172px; color: #fff; font-size: 15px; line-height: 19px; }
  .person-name strong { font-weight: 700; font-size: 15.5px; }
  .person-name span { display: block; font-size: 14px; font-weight: 400; }
  .person-name--doctor { top: 194px; }
  .person-name--physio { top: 549px; }
  .bio { position: absolute; left: 35px; width: 330px; font-size: 14.2px; line-height: 24.6px; text-align: justify; }
  .bio--doctor { top: 306px; }
  .bio--physio { top: 671px; }
  .site-url { position: absolute; left: 60px; top: 858px; font-size: 21px; font-weight: 700; color: var(--blue); font-stretch: 94%; }

  /* Photo */
  .hero-photo { position: absolute; left: 400px; top: 0; width: 800px; height: 493px;
    background: linear-gradient(120deg, var(--photo-light) 0%, #bdbdbd 35%, var(--photo-dark) 55%, #cfcfcf 75%, var(--photo-light) 100%); }
  .award-badge { position: absolute; left: 432px; top: 84px; width: 128px; height: 128px; border-radius: 50%; background: var(--badge); }

  /* Section bands */
  .section-band { position: absolute; height: 35px; color: #fff; font-weight: 700; font-stretch: 96%; }
  .section-band--services { left: 400px; top: 493px; width: 400px; background: var(--grey-band); font-size: 19px; padding: 4px 0 0 43px; }
  .section-band--physio { left: 800px; top: 458px; width: 398px; background: var(--blue-band); font-size: 19.5px; text-align: center; padding-top: 3px; }
  .notch { position: absolute; width: 0; height: 0; border-left: 8px solid transparent; border-right: 8px solid transparent; }
  .notch--services { left: 717px; top: 528px; border-top: 14px solid var(--grey-band); }
  .notch--physio { left: 1125px; top: 492px; border-top: 12px solid var(--blue-band); }

  /* Middle panel: services */
  .services { position: absolute; left: 443px; top: 549px; width: 315px; font-size: 14.2px; line-height: 24.5px; }
  .services p { text-align: justify; }
  .service-list { list-style: none; margin: 7px 0 6px; font-weight: 700; color: var(--list); line-height: 20.6px; }
  .service-list li::before { content: "• "; }

  /* Right panel: physio */
  .physio-copy { position: absolute; left: 842px; top: 511px; width: 315px; font-size: 14.2px; line-height: 24.6px; }
  .physio-copy p { text-align: justify; }
  .physio-copy h3 { font-size: 18px; font-weight: 700; color: var(--blue); margin: 8px 0 6px; font-stretch: 96%; line-height: 24px; }
</style>
</head>
<body>
<main class="spread">
  <div class="fold fold--one"></div>
  <div class="fold fold--two"></div>

  <section class="team">
    <h2 class="team-title">Our team leaders</h2>

    <div class="name-band name-band--blue"></div>
    <div class="portrait portrait--doctor" role="img" aria-label="Portrait of Dr. Harriet Osei, physiatrist"></div>
    <p class="person-name person-name--doctor"><strong>Harriet Osei,</strong><span>MD, FRCPC, MSC, CIME</span><span>Physiatrist</span></p>
    <p class="bio bio--doctor">Dr. Osei specializes in injury rehab and sports medicine. She is highly trained having received her MD and Residency in Physiatry from Wexmoor University. Her passion is to help injured people get back to their life.</p>

    <div class="name-band name-band--grey"></div>
    <div class="portrait portrait--physio" role="img" aria-label="Portrait of Dorothy Varga, physiotherapist"></div>
    <p class="person-name person-name--physio"><strong>Dorothy Varga, PT</strong><span>Physiotherapist</span></p>
    <p class="bio bio--physio">Dorothy has over 10 years of experience as a Physiotherapist (5 in Canada). She has advanced training in orthopedics and manual therapy. She loves and relates well with people from the youngest to the most senior.</p>

    <p class="site-url">www.velamotiongroup.ca</p>
  </section>

  <div class="hero-photo" role="img" aria-label="Black and white photo of a physiotherapist adjusting a knee brace on a patient's leg"></div>
  <div class="award-badge" aria-hidden="true"></div>

  <section>
    <h2 class="section-band section-band--services">Our services</h2>
    <div class="notch notch--services"></div>
    <div class="services">
      <p>We provide integrated assessment and care from interprofessional team of regulated healthcare professionals with proven experience in injury rehabilitation:</p>
      <ul class="service-list">
        <li>Physiatrists</li>
        <li>Sport medicine physicians</li>
        <li>Physiotherapists</li>
        <li>Chiropractors</li>
        <li>Massage therapists</li>
        <li>Acupuncturists</li>
        <li>Psychologists</li>
      </ul>
      <p>We provide custom medical bracing, orthotics, orthopedic shoes, assistive devices, and medical stockings, all in one place.</p>
    </div>
  </section>

  <section>
    <h2 class="section-band section-band--physio">Only registered physiotherapists</h2>
    <div class="notch notch--physio"></div>
    <div class="physio-copy">
      <p>We strongly believe in consistency with your treatment plan. This means that you spend your time here one-on-one with your physiotherapist, not any students or assistants. You get consistent high quality care from a professional.</p>
      <h3>One-on-one</h3>
      <p>&nbsp;attention We book maximum 3 people per hour to ensure everyone gets adequate one-on-one time with their physiotherapist. This compares favorably with other clinics, who may book upwards of 5-6 per hour. The atmosphere is professional -balanced with friendly, caring and relaxed. Our highly qualified staff operate this way to help make your recovery faster and more enjoyable.</p>
    </div>
  </section>
</main>
</body>
</html>
```